Einladungskarten
Zielgruppe
Wir sind die Gewerbeverbund Talbrück-Moos. Eine Organisation zur Interessenvertretung, Beratung und Unterstützung von Handwerksbetrieben. Unsere Zielgruppe sind Handwerksbetriebe.
Aufgabenstellung
Das Design soll modern sein. Es handelt sich um Einladungskarten zu einer Veranstaltung, die per Post verschickt werden sollen. Format: DIN Lang.
Die Veranstaltung hat den Titel: Brot, Käse und Chips
Einlass: 18:00 Uhr
Beginn: 18:30 Uhr
Adresse: Kickwiese Olmen - Lerchenweg 14, 41872 Olmen
Veranstalter: GVA vital und Gewerbeverbund Talbrück-Moos

```html
<!DOCTYPE html>
<html lang="de">
<head>
<meta charset="utf-8">
<title>Brot, Käse und Chips – Einladung</title>
<link href="https://fonts.googleapis.com/css2?family=Figtree:wght@400;600;700;800&display=swap" rel="stylesheet">
<style>
  :root {
    --page-bg: #e8edf3;
    --card-bg: #ffffff;
    --navy: #17468a;
    --accent: #3a8fd4;
    --ink: #222222;
    --crimson: #c8174f;
    --ice-light: #e6f3fc;
    --ice-mid: #a9d6f2;
    --ice-deep: #4aa3dc;
  }
  * { box-sizing: border-box; margin: 0; padding: 0; }
  html, body {
    width: 1200px; height: 1177px; overflow: hidden;
    background: var(--page-bg);
    font-family: "Figtree", Arial, sans-serif;
  }
  .invitation {
    position: absolute; left: 146px; top: 0;
    width: 908px; height: 1177px;
    background: var(--card-bg);
    overflow: hidden;
  }
  .frame-line { position: absolute; inset: 0; }
  .title {
    position: absolute; left: 0; right: 0; top: 146px;
    text-align: center; color: var(--navy);
    font-weight: 800; font-size: 94px; line-height: 87px;
    letter-spacing: -1px; text-transform: uppercase;
  }
  .schedule-row {
    position: absolute; left: 0; width: 100%; height: 62px;
  }
  .schedule-row.entry { top: 351px; }
  .schedule-row.start { top: 425px; }
  .schedule-label {
    position: absolute; right: 498px; top: 0; line-height: 62px;
    font-size: 48px; font-weight: 700; color: var(--ink);
  }
  .schedule-time {
    position: absolute; left: 421px; top: 0;
    width: 263px; height: 62px; border-radius: 8px;
    background: var(--accent); color: #fff;
    font-size: 48px; font-weight: 600; line-height: 62px; text-align: center;
  }
  .address-box {
    position: absolute; left: 168px; top: 553px;
    width: 572px; height: 58px;
    border: 3px solid var(--accent); border-radius: 10px;
  }
  .address-label {
    position: absolute; left: 50%; top: -22px; transform: translateX(-50%);
    background: var(--card-bg); padding: 0 14px;
    color: var(--crimson); font-weight: 700; font-size: 30px; line-height: 36px;
  }
  .address-text {
    position: absolute; left: 0; right: 0; top: 14px;
    text-align: center; font-size: 24px; color: var(--ink); line-height: 28px;
  }
  .organizer-heading {
    position: absolute; left: 0; right: 0; top: 667px;
    text-align: center; color: var(--navy); font-weight: 700; font-size: 29px;
  }
  .organizer-row { position: absolute; left: 0; right: 0; top: 711px; height: 92px; }
  .organizer-partner {
    position: absolute; left: 150px; width: 280px; top: 22px;
    text-align: center; font-size: 42px; font-weight: 700; color: var(--ink);
  }
  .organizer-divider {
    position: absolute; left: 452px; top: 0; width: 2px; height: 90px; background: var(--navy);
  }
  .organizer-host {
    position: absolute; left: 476px; top: 16px;
    display: flex; align-items: center; gap: 14px;
  }
  .host-mark { width: 54px; height: 54px; background: var(--navy); flex: none; }
  .host-name {
    font-size: 20px; font-weight: 700; color: var(--ink); line-height: 25px;
  }
  .ice-band { position: absolute; left: 0; bottom: 0; width: 908px; height: 400px; }
</style>
</head>
<body>
  <main class="invitation">
    <svg class="frame-line" width="908" height="1177" aria-hidden="true">
      <path d="M72 821 V72 H836 V846" fill="none" stroke="var(--accent)" stroke-width="5"/>
    </svg>

    <h1 class="title">Brot, Käse<br>und Chips</h1>

    <div class="schedule-row entry">
      <span class="schedule-label">Einlass:</span>
      <span class="schedule-time">18:00 Uhr</span>
    </div>
    <div class="schedule-row start">
      <span class="schedule-label">Beginn:</span>
      <span class="schedule-time">18:30 Uhr</span>
    </div>

    <div class="address-box">
      <span class="address-label">Adresse:</span>
      <p class="address-text">Kickwiese Olmen - Lerchenweg 14, 41872 Olmen</p>
    </div>

    <h2 class="organizer-heading">Veranstalter:</h2>
    <div class="organizer-row">
      <span class="organizer-partner">GVA vital</span>
      <span class="organizer-divider"></span>
      <div class="organizer-host">
        <span class="host-mark"></span>
        <span class="host-name">Gewerbeverbund<br>Talbrück-Moos</span>
      </div>
    </div>

    <svg class="ice-band" viewBox="0 777 908 400" role="img" aria-label="Dekoratives Muster aus hellblauen Polygonflächen">
      <defs>
        <linearGradient id="ice-fill" x1="0" y1="0" x2="0" y2="1">
          <stop offset="0" stop-color="var(--ice-light)"/>
          <stop offset="0.45" stop-color="var(--ice-mid)"/>
          <stop offset="1" stop-color="var(--ice-deep)"/>
        </linearGradient>
      </defs>
      <polygon points="0,793 169,897 425,910 620,984 732,895 908,777 908,1177 0,1177" fill="url(#ice-fill)"/>
    </svg>
  </main>
</body>
</html>
```